Holzdesign Firma sucht stilvolles Corporate Design
Zielgruppe
Ich stelle Utensilien aus Holz für die Küche her und verkaufe diese übers Internet. In erster Linie platzsparende Messerbretter aus Holz. Meine Zielgruppe ist jeder in Deutschland der eine Küche hat und dort kocht.
Aufgabenstellung
Das Design sollte eher schlicht und innovativ wirken. Der Name FELDRUNE muss mit ihm Logo sein. Im Logo sollte auch eine Verbindung zum Holz erkennbar sein, am besten mit einem Holzbalken oder einem Baumstamm. Im Logo sollen keine Weihnachtsbäume oder ganze Bäume sichtbar sein. Die Farbwahl würde ich auf Farben die zu Holz und Natur passen eingrenzen.
Mit dem Design will ich mich von den übrigen Handwerksbetrieben abheben und nicht einfach die üblichen Standarddesigns kopieren.

```html
<!DOCTYPE html>
<html lang="de">
<head>
<meta charset="utf-8">
<title>FELDRUNE – Geschäftsausstattung</title>
<link href="https://fonts.googleapis.com/css2?family=Barlow:wght@300;400;600&family=Kaushan+Script&display=swap" rel="stylesheet">
<style>
:root{
  --orange:#e84e1b;
  --brown:#4a2a14;
  --ink:#3a2a20;
  --label:#8a8a8a;
  --paper:#ffffff;
  --bg-top:#f6f6f6;
  --bg-bottom:#e9e9e9;
  --window:#a9a9a9;
}
*{margin:0;padding:0;box-sizing:border-box}
html,body{width:1200px;height:801px;overflow:hidden}
body{position:relative;background:linear-gradient(180deg,var(--bg-top),var(--bg-bottom));font-family:"Barlow",sans-serif;color:var(--ink)}
.sheet{position:absolute;background:var(--paper);box-shadow:0 6px 14px rgba(0,0,0,.16)}
.wordmark{position:absolute;text-align:center;transform:translateX(-50%);white-space:nowrap}
.wordmark__name{display:block;font-weight:600;color:var(--orange);letter-spacing:.04em;line-height:1}
.wordmark__slogan{display:block;color:var(--brown);font-weight:400}
.wordmark--hero{left:325px;top:98px}
.wordmark--hero .wordmark__name{font-size:46px}
.wordmark--hero .wordmark__slogan{font-size:10.5px;margin-top:10px;letter-spacing:.03em}
.label{position:absolute;top:263px;font-weight:300;font-size:15px;color:var(--label);transform:translateX(-50%)}
.card-front{left:58px;top:292px;width:259px;height:167px}
.card-front .wordmark{left:129px;top:64px}
.card-front .wordmark__name{font-size:30px}
.card-front .wordmark__slogan{font-size:6.5px;margin-top:6px}
.card-back{left:333px;top:292px;width:259px;height:167px;text-align:center}
.card-back__name{position:absolute;left:0;right:0;top:44px;font-family:"Kaushan Script",cursive;color:var(--orange);font-size:15px}
.card-back__role{position:absolute;left:0;right:0;top:67px;font-size:8px;color:var(--ink)}
.card-back__rule{position:absolute;left:22px;top:100px}
.card-back__contact{position:absolute;left:0;right:0;top:116px;font-size:8px;line-height:12.7px;letter-spacing:.02em}
.envelope{left:58px;top:497px;width:536px;height:266px}
.envelope .wordmark{left:150px;top:46px}
.envelope .wordmark__name{font-size:22px}
.envelope .wordmark__slogan{font-size:5px;margin-top:4px}
.envelope__window{position:absolute;left:47px;top:120px;width:206px;height:111px;border-radius:10px;background:linear-gradient(135deg,var(--window),#bdbdbd 60%,#9c9c9c)}
.letter{left:630px;top:34px;width:520px;height:736px;font-size:6.5px;line-height:10.5px}
.letter .wordmark{left:260px;top:48px}
.letter .wordmark__name{font-size:22px}
.letter .wordmark__slogan{font-size:4.5px;margin-top:4px}
.fold{position:absolute;left:0;width:8px;height:1px;background:var(--orange)}
.brand-small{color:var(--orange);font-weight:600;letter-spacing:.04em}
.letter__sender{position:absolute;left:60px;top:158px;font-size:5px}
.letter__recipient{position:absolute;left:62px;top:176px;line-height:12.5px}
.letter__contact{position:absolute;right:33px;top:136px;text-align:right;font-size:6px;line-height:10.4px}
.letter__contact .gap{height:6px}
.letter__subject{position:absolute;left:62px;top:245px}
.letter__body{position:absolute;left:62px;top:277px;width:420px}
.letter__body p{margin-bottom:10.5px}
.letter__rule{position:absolute;left:35px;top:660px}
.letter__footer{position:absolute;top:689px;font-size:5.8px;line-height:10.4px}
.letter__footer--a{left:48px}
.letter__footer--b{left:188px}
.letter__footer--c{left:364px}
</style>
</head>
<body>

<div class="wordmark wordmark--hero">
  <span class="wordmark__name">FELDRUNE</span>
  <span class="wordmark__slogan">Hier könnte Ihr Slogan stehen.</span>
</div>

<span class="label" style="left:187px">Visitenkarte vorne</span>
<span class="label" style="left:463px">Visitenkarte hinten</span>

<section class="sheet card-front">
  <div class="wordmark">
    <span class="wordmark__name">FELDRUNE</span>
    <span class="wordmark__slogan">Hier könnte Ihr Slogan stehen.</span>
  </div>
</section>

<section class="sheet card-back">
  <div class="card-back__name">Jonas Beispielmann</div>
  <div class="card-back__role">Position</div>
  <svg class="card-back__rule" width="224" height="8" viewBox="0 0 224 8"><path d="M2 5 C60 2,150 2,222 3" stroke="var(--brown)" stroke-width="3" fill="none" stroke-linecap="round"/></svg>
  <div class="card-back__contact">Ahornweg 12a, 45870 Waldstadt<br>Tel.: 0261 730415<br>j.beispielmann@feldrune-beispiel.de</div>
</section>

<section class="sheet envelope">
  <div class="wordmark">
    <span class="wordmark__name">FELDRUNE</span>
    <span class="wordmark__slogan">Hier könnte Ihr Slogan stehen.</span>
  </div>
  <div class="envelope__window"></div>
</section>

<section class="sheet letter">
  <div class="wordmark">
    <span class="wordmark__name">FELDRUNE</span>
    <span class="wordmark__slogan">Hier könnte Ihr Slogan stehen.</span>
  </div>
  <span class="fold" style="top:260px"></span>
  <span class="fold" style="top:369px"></span>
  <span class="fold" style="top:521px"></span>

  <div class="letter__sender"><span class="brand-small">FELDRUNE</span> | Ahornweg 9 | 45870 Waldstadt</div>
  <div class="letter__recipient">Herr Beispielmann<br>Birkenstraße 3<br>48560 Feldheim</div>

  <div class="letter__contact">
    <span class="brand-small" style="font-size:7.5px">FELDRUNE</span><br>
    Eichenallee 41<br>55560 Waldstadt
    <div class="gap"></div>
    Tel.: 0261 730415<br>Fax: 0261 730416<br>Mobil: 0176 4418203
    <div class="gap"></div>
    info@feldrune-beispiel.de<br>www.feldrune-beispiel.de
  </div>

  <div class="letter__subject">Hier steht eine Betreffzeile</div>
  <div class="letter__body">
    <p style="margin-top:20px">Sehr geehrte Frau Lindenhof,</p>
    <p>als Kunde unseres jungen und modernen Unternehmens erwartet<br>Sie Qualität in höchstem Maße.</p>
    <p>Sie können sicher zu sein, genau zu bekommen, was wir Ihnen versprechen.<br>Und damit werden Sie auch rundum zufrieden sein. Das garantieren wir Ihnen.</p>
    <p>Schauen Sie doch gleich das beiliegende Prospekt. Wir bieten Ihnen moderne und hochwertige Produkte, die auf dem neuesten Stand der Technik sind, an. Überzeugen Sie sich selbst von der hochwertigen Qualität unserer Produkte und bestellen Sie noch heute.</p>
    <p>Wir freuen uns auf Ihre Bestellung und sind bei Rückfragen gerne für Sie da.</p>
    <p>Mit freundlichen Grüßen</p>
  </div>

  <svg class="letter__rule" width="464" height="12" viewBox="0 0 464 12"><path d="M2 7 C120 4,260 -2,350 4 C410 8,445 10,462 4" stroke="var(--brown)" stroke-width="3" fill="none" stroke-linecap="round"/></svg>

  <div class="letter__footer letter__footer--a"><span class="brand-small">FELDRUNE</span><br>Ahornweg 9<br>45870 Waldstadt</div>
  <div class="letter__footer letter__footer--b">USt-IDNR: DE4410277<br>Steuernummer: 184/310/552<br>Inhaber: Jonas Beispielmann</div>
  <div class="letter__footer letter__footer--c">Kreisbank Waldstadt<br>IBAN: DE00 1234 5678 9000 0042<br>BIC: KRWADEXX01</div>
</section>

</body>
</html>
```